E-commerce Website - new look and feel

Link to website
http://198.51.100.42/~brontava/brontavale_ecommerce/index.php#

Home page
-Header
- -Search bar and add to cart
-Drop down - Multi layer category representation: 1st main category level in menu bar style, 2nd category to follow and 3rd category
-Banner
-Footer

-Search listing

Category page
-Product listing
-

Product detail page
-Product variation tabular view
-

Checkout page
-

404 link/product image not found
Should be fun and engaging customers

Recent search products/ preferred products for customers

all pages:
Headroom js search bar once you are lower down the page

Shrinking navbar

Target Market(s)

Telecommunication installers, electricians working on Industrial plants and projects, on the move customers that need immediate products, procurement officers buying for projects, hard to get items customers, Car hobbyists ( future market ) for some specific product like stainless steel braid(sleeve)

Industry/Entity Type

Telecommunications

Number of Pages Required

5+ page

Colors

Designer to choose colors to be used in the design.

Requirements
Must have
• - less cluttered design
• - Easy to navigate
• - more white area on all pages
• - quick orders
• - repetitive product ordering by customers menu/list
• - branding consistency, logo colours and design
Nice to have
• -modern look
• -user friendly for less technical and computer skilled customers
• -quick to navigate
• - fun text to make customer feel at ease when navigating through website
Should not have
• -too much details
• -

```html
<!DOCTYPE html>
<html lang="en">
<head>
<meta charset="utf-8">
<title>Brontavale Asia Pacific – Home</title>
<link rel="stylesheet" href="https://fonts.googleapis.com/css2?family=Open+Sans:wght@400;600;700&family=Roboto+Condensed:wght@400;700&display=swap">
<style>
:root{
  --blue:#1f8fd6;
  --blue-dark:#136fb0;
  --navy:#163a5f;
  --ink:#2d3a46;
  --muted:#7b8794;
  --line:#dfe5ea;
  --paper:#ffffff;
  --soft:#f3f6f8;
  --btn:#1c86cf;
}
*{box-sizing:border-box;margin:0;padding:0}
html,body{width:730px;height:1200px;overflow:hidden}
body{font-family:"Open Sans",Arial,sans-serif;color:var(--ink);background:var(--paper);position:relative}
.cond{font-family:"Roboto Condensed","Arial Narrow",sans-serif}

/* top strip */
.topbar{height:22px;display:flex;justify-content:flex-end;align-items:center;gap:14px;padding-right:12px}
.topbar .phone{font-size:10px;color:var(--blue);font-weight:700;display:flex;align-items:center;gap:4px}
.topbar .help{background:var(--blue);color:#fff;font-size:8px;font-weight:700;padding:6px 10px;text-transform:uppercase;height:22px}

/* header */
.header{height:82px;display:flex;justify-content:space-between;align-items:flex-start;padding:10px 20px 0 26px}
.brand{display:flex;align-items:center;gap:8px;margin-top:8px}
.brand .mark{width:30px;height:30px;border-radius:50%;background:var(--blue)}
.brand .name{font-size:26px;font-weight:700;color:var(--navy);line-height:1;letter-spacing:.5px}
.brand .sub{font-size:10px;font-weight:700;color:var(--navy);letter-spacing:1.5px;margin-top:3px}
.account{text-align:right}
.account ul{list-style:none;display:flex;gap:12px;font-size:8.5px;font-weight:700;text-transform:uppercase;color:var(--ink);margin-top:6px}
.account li::before{content:"";display:inline-block;width:7px;height:7px;border-radius:50%;background:var(--blue);margin-right:4px;vertical-align:-1px}
.search{margin:14px 0 0 auto;width:155px;height:20px;border:1px solid var(--line);font-size:8px;color:var(--muted);display:flex;align-items:center;justify-content:space-between;padding:0 6px}

/* nav */
.nav{height:24px;background:var(--blue);display:flex;align-items:center;padding:0 12px;color:#fff;font-size:8px;font-weight:700;text-transform:uppercase}
.nav .cat{display:flex;align-items:center;gap:6px;padding-right:14px}
.nav ul{list-style:none;display:flex;gap:20px}
.nav .social{margin-left:auto;display:flex;gap:6px}
.nav .social span{width:9px;height:9px;background:#fff;opacity:.9;border-radius:2px}

/* hero */
.hero{height:310px;position:relative;background:linear-gradient(120deg,#5a86a8 0%,#9bb9d0 35%,#c9d8e3 55%,#6f94b3 80%,#d8e2ea 100%)}
.hero .copy{position:absolute;left:26px;top:96px;color:#fff}
.hero .welcome{font-size:18px;font-weight:700;text-transform:uppercase}
.hero h1{font-size:44px;font-weight:700;text-transform:uppercase;line-height:1}
.hero p{font-size:8px;width:240px;margin:6px 0 14px;line-height:1.35}
.btn{display:inline-block;background:var(--btn);color:#fff;font-size:7.5px;font-weight:700;text-transform:uppercase;padding:5px 12px;border-radius:2px}

/* tiles */
.tiles{position:absolute;left:0;right:0}
.row1{top:470px;height:195px;display:flex;gap:4px}
.row2{top:670px;height:190px;display:flex;gap:4px}
.tile{position:relative;overflow:hidden}
.tile .txt{position:absolute;color:#fff;font-weight:700;text-transform:uppercase;line-height:1}
.tile .small{font-size:10px}
.tile .big{font-size:21px}

.t-eth{width:245px;background:linear-gradient(160deg,#f7f7f0 0%,#e8e6c8 40%,#dcd9b0 100%)}
.t-eth .txt{left:12px;top:100px;color:var(--navy)}
.t-cat{flex:1;background:linear-gradient(135deg,#0f4f85 0%,#1b6fb0 45%,#2a8bd0 100%)}
.t-cat .txt{right:14px;top:38px;text-align:right}
.t-sec{width:235px;background:linear-gradient(150deg,#e9eef2 0%,#cfd8df 60%,#b9c6d0 100%)}
.t-sec .txt{left:12px;top:20px;color:var(--navy)}
.t-blog{width:255px;background:linear-gradient(135deg,#0c3d36 0%,#177a62 50%,#0e4f44 100%)}
.t-blog .txt{right:14px;top:18px;text-align:right;font-size:9px}
.t-col{flex:1;background:linear-gradient(150deg,#eef2f5 0%,#5b9bd1 45%,#d6453c 70%,#33383d 100%)}
.t-col .txt{right:14px;top:20px;text-align:right}

/* feature band */
.band{position:absolute;top:865px;left:0;right:0;height:44px;background:var(--blue);display:flex;align-items:center;justify-content:space-around;color:#fff}
.feat{display:flex;align-items:center;gap:8px}
.feat b{display:block;font-size:13px;text-transform:uppercase;line-height:1}
.feat small{display:block;font-size:7px;text-transform:uppercase}

/* footer */
.footer{position:absolute;top:920px;left:20px;right:20px;display:grid;grid-template-columns:200px 130px 160px 1fr;gap:22px}
.footer h4{font-size:10px;font-weight:700;text-transform:uppercase;border-bottom:1px solid var(--line);padding-bottom:5px;margin-bottom:8px}
.form .pair{display:flex;gap:6px;margin-bottom:6px}
.field{border:1px solid var(--line);height:18px;font-size:6.5px;color:var(--muted);padding:4px 5px;flex:1;text-transform:uppercase}
.field.area{height:60px}
.form .btn{float:right;margin-top:6px}
.links ul{list-style:none;font-size:7px;text-transform:uppercase;color:var(--muted);line-height:2.4}
.pay{display:grid;grid-template-columns:repeat(4,30px);gap:5px}
.pay span{height:18px;border:1px solid var(--line);border-radius:2px;background:var(--soft)}
.contact p{font-size:7px;color:var(--muted);display:flex;gap:6px;margin-bottom:9px;line-height:1.3}
.contact i{width:9px;height:9px;border-radius:50%;background:var(--blue);flex:none}

/* newsletter */
.news{position:absolute;top:1135px;left:0;right:0;height:40px;background:var(--blue);display:flex;align-items:center;padding:0 20px;color:#fff}
.news .label{display:flex;align-items:center;gap:10px;font-size:12px;font-weight:700;text-transform:uppercase}
.news .form-in{margin-left:auto;display:flex}
.news .input{width:200px;height:18px;background:#fff}
.news .sub{background:var(--navy);font-size:7px;font-weight:700;padding:5px 8px;text-transform:uppercase}

.copy-line{position:absolute;top:1180px;left:20px;right:20px;font-size:7px;color:var(--muted);display:flex;justify-content:space-between;align-items:center}
.copy-line .up{width:12px;height:12px;background:var(--line)}
</style>
</head>
<body>

<div class="topbar">
  <span class="phone">
    <svg width="9" height="9" viewBox="0 0 24 24"><path fill="#1f8fd6" d="M6.6 10.8a15 15 0 0 0 6.6 6.6l2.2-2.2a1 1 0 0 1 1-.25 11.4 11.4 0 0 0 3.6.57 1 1 0 0 1 1 1V20a1 1 0 0 1-1 1A17 17 0 0 1 3 4a1 1 0 0 1 1-1h3.5a1 1 0 0 1 1 1c0 1.25.2 2.45.57 3.57a1 1 0 0 1-.25 1z"/></svg>
    1300 555 018
  </span>
  <span class="help">Need parts? Call our help</span>
</div>

<header class="header">
  <div class="brand">
    <span class="mark"></span>
    <div>
      <div class="name cond">BRONTAVALE</div>
      <div class="sub">ASIA PACIFIC PTY LTD</div>
    </div>
  </div>
  <div class="account">
    <ul>
      <li>My Account</li><li>My Wishlist</li><li>My Cart</li><li>Checkout</li><li>Log In</li>
    </ul>
    <div class="search">
      <span>Search Product</span>
      <svg width="8" height="8" viewBox="0 0 24 24"><circle cx="10" cy="10" r="7" fill="none" stroke="#7b8794" stroke-width="3"/><path d="M15 15l6 6" stroke="#7b8794" stroke-width="3"/></svg>
    </div>
  </div>
</header>

<nav class="nav">
  <div class="cat">
    <svg width="10" height="8" viewBox="0 0 10 8"><path d="M0 1h10M0 4h10M0 7h10" stroke="#fff" stroke-width="1.4"/></svg>
    Our Category
  </div>
  <ul><li>Home</li><li>About</li><li>Products</li><li>Blog</li><li>Learning Center</li><li>Contact Us</li></ul>
  <div class="social"><span></span><span></span><span></span><span></span></div>
</nav>

<section class="hero" role="img" aria-label="Photo of blue network cables plugged into a patch panel">
  <div class="copy">
    <div class="welcome cond">Welcome to</div>
    <h1 class="cond">Cat5e Cabling</h1>
    <p>Quality network cable for every install, shipped fast so your project keeps moving today.</p>
    <span class="btn">Shop Now</span>
  </div>
</section>

<div class="tiles row1">
  <div class="tile t-eth" role="img" aria-label="Photo of a coiled yellow ethernet cable">
    <div class="txt cond"><div class="small">Top Quality</div><div class="big">Ethernet Cable</div><span class="btn" style="margin-top:8px">Shop Now</span></div>
  </div>
  <div class="tile t-cat" role="img" aria-label="Photo of blue network cables in a server rack">
    <div class="txt cond"><div class="small">Shop for</div><div class="big">Catsecable</div><span class="btn" style="margin-top:8px">Shop Now</span></div>
  </div>
</div>

<div class="tiles row2">
  <div class="tile t-sec" role="img" aria-label="Photo of stripped white security cable with coloured wires">
    <div class="txt cond"><div class="small">Super Fast</div><div class="big">Security Cable</div><span class="btn" style="margin-top:8px">Shop Now</span></div>
  </div>
  <div class="tile t-blog" role="img" aria-label="Photo of a green circuit board">
    <div class="txt cond"><div>Visit Our</div><div style="font-size:14px">Blog</div><span class="btn" style="margin-top:8px">Visit Blog</span></div>
  </div>
  <div class="tile t-col" role="img" aria-label="Photo of coloured cable reels">
    <div class="txt cond"><div class="small">Wide Range of</div><div class="big">Color Cables</div><span class="btn" style="margin-top:8px">Shop Now</span></div>
  </div>
</div>

<div class="band">
  <div class="feat">
    <svg width="22" height="18" viewBox="0 0 22 18"><rect x="1" y="1" width="20" height="16" rx="2" fill="none" stroke="#fff" stroke-width="2"/><path d="M1 6h20" stroke="#fff" stroke-width="3"/></svg>
    <div><b class="cond">Secure Payment</b><small>Affordable Price</small></div>
  </div>
  <div class="feat">
    <svg width="26" height="18" viewBox="0 0 26 18"><rect x="1" y="2" width="15" height="11" fill="#fff"/><path d="M16 6h5l4 4v3h-9z" fill="#fff"/><circle cx="6" cy="15" r="2.5" fill="#fff"/><circle cx="20" cy="15" r="2.5" fill="#fff"/></svg>
    <div><b class="cond">Free Home Delivery</b><small>Orders $50 &amp; Over</small></div>
  </div>
  <div class="feat">
    <svg width="18" height="18" viewBox="0 0 24 24"><path fill="#fff" d="M6.6 10.8a15 15 0 0 0 6.6 6.6l2.2-2.2a1 1 0 0 1 1-.25 11.4 11.4 0 0 0 3.6.57 1 1 0 0 1 1 1V20a1 1 0 0 1-1 1A17 17 0 0 1 3 4a1 1 0 0 1 1-1h3.5a1 1 0 0 1 1 1c0 1.25.2 2.45.57 3.57a1 1 0 0 1-.25 1z"/></svg>
    <div><b class="cond">1300 555 018</b><small>Toll Free to Call Us</small></div>
  </div>
</div>

<footer class="footer">
  <div class="form">
    <h4 class="cond">Send Message</h4>
    <div class="pair"><div class="field">Name</div><div class="field">Email</div></div>
    <div class="field area">Message</div>
    <span class="btn">Send Message</span>
  </div>
  <div class="links">
    <h4 class="cond">Usefull Links</h4>
    <ul><li>My Account</li><li>Ordering &amp; Payment</li><li>Delivery Information</li><li>Returns Policy</li><li>Shipping Status</li></ul>
  </div>
  <div>
    <h4 class="cond">Payment Methode</h4>
    <div class="pay"><span></span><span></span><span></span><span></span><span></span><span></span><span></span><span></span></div>
  </div>
  <div class="contact">
    <h4 class="cond">Contact Us</h4>
    <p><i></i>123 Street Name<br>City Name, Country</p>
    <p><i></i>1300 555 018</p>
    <p><i></i>info@email.com</p>
  </div>
</footer>

<div class="news">
  <div class="label cond">
    <svg width="20" height="14" viewBox="0 0 20 14"><rect x="1" y="1" width="18" height="12" fill="none" stroke="#fff" stroke-width="1.6"/><path d="M1 1l9 7 9-7" fill="none" stroke="#fff" stroke-width="1.6"/></svg>
    Sign up for newsletter to get updates
  </div>
  <div class="form-in"><span class="input"></span><span class="sub">Subscribe</span></div>
</div>

<div class="copy-line"><span>Copyright © 2017 eBrontavale, All rights reserved.</span><span class="up"></span></div>

</body>
</html>
```